Business card design for a dynamic IT consulting company

We need a business card design for a young firm, specialized in the Telecommunications/Consulting industry. The name of the company is Brask and Partners Business Consulting Ltd. (Short name: Brask and Partnes)
Brask = solve read reverse, so we aim to be uncomplicated and solution-oriented. The small pipe in our logo is also related to the word solve. So we need a new business card design, which is simple, eye catching and something non traditional (I would probably prefer a square shaped design rather than a rectangle, but open for suggestions). Attached our logo.

Target Market(s)

Usually our customers are Tier1 Telecoms providers (Q-Linkra, Parnexo, etc) and their executives.

Industry/Entity Type

Business

Contact Information for Business Card

Name: Gergely Halmindo
Email: g.halmindo@braskpartnera.hu
Web: www.braskpartnera.hu
Mobile: +36 30 555 0192
Title: Managing Director

Optional:
Company name: Brask and Partners Ltd.
Address: 1047 Budapest, Ravaszi str. 17/B, Hungary

Font styles to use
Other font styles liked:
• helveticaneue_medium, Prime Regular are used now.

Colors

Designer to choose colors to be used in the design.

Requirements
Must have
• I would like to have a 2 sided design.
Nice to have
• I thought if we make the logo a bit bigger (without the company name), that could go to the back with the company name below. I though, if the pipe in the logo is somehow touchable on the business card, would be nice and unique.

```html
<!DOCTYPE html>
<html lang="en">
<head>
<meta charset="utf-8">
<title>Brask &amp; Partners – Business Card</title>
<link rel="stylesheet" href="https://fonts.googleapis.com/css2?family=Open+Sans:wght@700&family=Titillium+Web:wght@300&display=swap">
<style>
  :root {
    --backdrop: #3f3f41;
    --card: #272e3b;
    --card-edge: #313848;
    --ink: #ffffff;
    --accent-blue: #2aa7e0;
    --accent-magenta: #8a2f73;
    --accent-grey: #8c9097;
  }
  * { box-sizing: border-box; margin: 0; padding: 0; }
  html, body { width: 1200px; height: 801px; overflow: hidden; }
  body { background: var(--backdrop); position: relative; font-family: "Open Sans", sans-serif; }

  .card {
    position: absolute;
    top: 250px;
    width: 478px;
    height: 276px;
    border-radius: 14px;
    background: var(--card);
    box-shadow: 0 0 0 1px var(--card-edge), 0 6px 18px rgba(0,0,0,.45);
    overflow: hidden;
  }
  .card--front { left: 114px; }
  .card--back  { left: 610px; }

  .pattern {
    position: absolute;
    width: 136px;
    height: 100px;
  }
  .pattern--top-left {
    left: 2px; top: 2px;
    background: linear-gradient(135deg, rgba(42,167,224,.28), rgba(138,47,115,.22) 55%, rgba(39,46,59,0));
  }
  .pattern--bottom-right {
    right: 2px; bottom: 0;
    background: linear-gradient(315deg, rgba(138,47,115,.28), rgba(42,167,224,.24) 55%, rgba(39,46,59,0));
  }

  .brand {
    position: absolute;
    top: 113px;
    left: 0; right: 0;
    display: flex;
    align-items: center;
    justify-content: center;
    gap: 12px;
  }
  .brand__square {
    width: 16px; height: 16px;
    background: var(--accent-blue);
  }
  .brand__name {
    font-family: "Titillium Web", sans-serif;
    font-weight: 300;
    font-size: 36px;
    line-height: 1;
    color: var(--ink);
    letter-spacing: .5px;
  }

  .holder {
    position: absolute;
    top: 24px;
    right: 43px;
    text-align: right;
    font-weight: 700;
    line-height: 1;
  }
  .holder__name { font-size: 11.5px; color: var(--accent-blue); letter-spacing: .2px; }
  .holder__title { font-size: 10px; color: var(--ink); margin-top: 7px; }

  .contacts {
    position: absolute;
    left: 196px;
    top: 204px;
    list-style: none;
  }
  .contacts__item {
    display: flex;
    align-items: center;
    gap: 9px;
    height: 19px;
    font-size: 12px;
    font-weight: 700;
    color: var(--ink);
  }
  .contacts__icon { width: 15px; height: 13px; flex: none; }
</style>
</head>
<body>

  <section class="card card--front" aria-label="Card front">
    <div class="pattern pattern--top-left" role="img" aria-label="Decorative pattern of small coloured squares"></div>
    <div class="pattern pattern--bottom-right" role="img" aria-label="Decorative pattern of small coloured squares"></div>
    <div class="brand">
      <span class="brand__square"></span>
      <span class="brand__name">Brask &amp; Partners</span>
    </div>
  </section>

  <section class="card card--back" aria-label="Card back">
    <div class="pattern pattern--top-left" role="img" aria-label="Decorative pattern of small coloured squares"></div>
    <div class="pattern pattern--bottom-right" role="img" aria-label="Decorative pattern of small coloured squares"></div>

    <div class="holder">
      <p class="holder__name">GERGELY HALMINDO</p>
      <p class="holder__title">MANAGING DIRECTOR</p>
    </div>

    <div class="brand">
      <span class="brand__square"></span>
      <span class="brand__name">Brask &amp; Partners</span>
    </div>

    <ul class="contacts">
      <li class="contacts__item">
        <svg class="contacts__icon" viewBox="0 0 15 13" aria-hidden="true">
          <path d="M1 4 Q7.5 0 14 4 L12 5.5 L10.5 4 L4.5 4 L3 5.5 Z" fill="none" stroke="#2aa7e0" stroke-width="1.2"/>
          <rect x="3" y="6.5" width="9" height="5.5" rx="1" fill="none" stroke="#2aa7e0" stroke-width="1.2"/>
          <circle cx="7.5" cy="9.2" r="1.3" fill="#2aa7e0"/>
        </svg>
        +36 30 555 0192
      </li>
      <li class="contacts__item">
        <svg class="contacts__icon" viewBox="0 0 15 13" aria-hidden="true">
          <rect x="1" y="2" width="13" height="9" fill="none" stroke="#2aa7e0" stroke-width="1.2"/>
          <path d="M1 2 L7.5 7.5 L14 2" fill="none" stroke="#2aa7e0" stroke-width="1.2"/>
        </svg>
        g.halmindo@braskpartnera.hu
      </li>
      <li class="contacts__item">
        <svg class="contacts__icon" viewBox="0 0 15 13" aria-hidden="true">
          <circle cx="7.5" cy="6.5" r="5.5" fill="none" stroke="#2aa7e0" stroke-width="1.1"/>
          <ellipse cx="7.5" cy="6.5" rx="2.3" ry="5.5" fill="none" stroke="#2aa7e0" stroke-width="1"/>
          <path d="M2 6.5 H13" stroke="#2aa7e0" stroke-width="1"/>
        </svg>
        www.braskpartnera.hu
      </li>
    </ul>
  </section>

</body>
</html>
```